Web Developer Needs a Business Card Design

I need a personal business card design that represents me as a web developer for potential employers. I would like the background to be a dark color on the front for contrast with my logo and name. The back will have all my information along with a smaller version of the logo. I want something with a modern look and feel, not too conservative. This will be used for potential employers and freelance work.

Industry/Entity Type

Business

Contact Information for Business Card

Front should have my logo and name. The back should have all my personal information which would include: name: Tom Brevardi, phone: 570-614-9083, email: tombrevardi@mailwisp.com, website url: www.tombrevardi.com, logo, web developer.

Font styles to use
Sans Serif

Requirements
Must have
• Must include my logo. The color palette base color will be the logo color.

```html
<!DOCTYPE html>
<html lang="en">
<head>
<meta charset="utf-8">
<title>Tom Brevardi — Business Card</title>
<link rel="stylesheet" href="https://fonts.googleapis.com/css2?family=Roboto:wght@400;500&display=swap">
<style>
  :root {
    --backdrop: #a8a5a5;
    --mint: #50e0bd;
    --card-black: #0c0c0c;
    --photo-dark: #151515;
    --white: #f4f4f4;
  }
  * { box-sizing: border-box; margin: 0; padding: 0; }
  html, body {
    width: 1200px; height: 1200px; overflow: hidden;
    background: var(--backdrop);
    font-family: "Roboto", Arial, sans-serif;
  }
  .canvas {
    position: relative; width: 1200px; height: 1200px;
  }
  .card {
    position: absolute; left: 244px; width: 706px; height: 418px;
    background: var(--mint);
    border-radius: 28px;
    padding: 18px;
  }
  .card--front { top: 118px; }
  .card--back { top: 644px; }
  .card__panel {
    position: relative; width: 100%; height: 100%;
    background: var(--card-black);
    border-radius: 18px;
    overflow: hidden;
  }
  .card__photo {
    position: absolute; inset: 0;
    background:
      radial-gradient(ellipse 30% 45% at 14% 55%, var(--photo-dark), transparent 70%),
      radial-gradient(ellipse 25% 35% at 88% 25%, var(--photo-dark), transparent 70%),
      var(--card-black);
  }
  .card__content {
    position: absolute; inset: 0;
    display: flex; flex-direction: column; align-items: center;
    text-align: center;
  }
  .brand {
    margin-top: 170px;
    display: flex; align-items: center; gap: 16px;
  }
  .brand__dot {
    width: 36px; height: 36px; border-radius: 50%;
    border: 6px solid var(--mint);
  }
  .brand__name {
    color: var(--mint); font-size: 38px; font-weight: 500; letter-spacing: 0.5px;
  }
  .contact__name {
    margin-top: 90px;
    color: var(--white); font-size: 34px; font-weight: 400; letter-spacing: 0.5px;
  }
  .contact__role {
    margin-top: 10px;
    color: var(--mint); font-size: 18px;
  }
  .contact__phone {
    margin-top: 70px;
    color: var(--mint); font-size: 19px;
  }
  .contact__links {
    margin-top: 8px;
    color: var(--mint); font-size: 19px; letter-spacing: 0.2px;
  }
  .contact__divider { margin: 0 18px; }
</style>
</head>
<body>
<main class="canvas">
  <section class="card card--front">
    <div class="card__panel">
      <div class="card__photo" role="img" aria-label="Dimmed overhead photo of a desk with a keyboard, tablet and notebook"></div>
      <div class="card__content">
        <div class="brand">
          <span class="brand__dot"></span>
          <span class="brand__name">Tom Brevardi</span>
        </div>
      </div>
    </div>
  </section>

  <section class="card card--back">
    <div class="card__panel">
      <div class="card__photo" role="img" aria-label="Dimmed overhead photo of a desk with a keyboard, tablet and notebook"></div>
      <div class="card__content">
        <h1 class="contact__name">Tom Brevardi</h1>
        <p class="contact__role">Web Developer</p>
        <p class="contact__phone">570-614-9083</p>
        <p class="contact__links">tombrevardi@mailwisp.com<span class="contact__divider">|</span>www.tombrevardi.com</p>
      </div>
    </div>
  </section>
</main>
</body>
</html>
```